Building company needs a letterhead design

I'm after a modern but professional letter head.
Must have the below details:
- Logo
- Website - TARVELBUILD.COM.AU
- Email - INFO@TARVELBUILD.COM.AU
- Office - 03 52631848
- Mobile number - 0413596281
- ABN - 47 318 965 102
...........................................................................................................................................................................................................................
- Logo
- Office - 03 52631848
- ABN - 47 318 965 102

Target Market(s)

.

Industry/Entity Type

Construction Company

Font styles to use
Sans Serif

Requirements
Must have
• Must have the below details:
• - Logo
• - Website - TARVELBUILD.COM.AU
• - Email - INFO@TARVELBUILD.COM.AU
• - Office - 03 52631848
• - Mobile number - 0413596281
• - ABN - 47 318 965 102
Nice to have
• .
Should not have
• .

```html
<!DOCTYPE html>
<html lang="en">
<head>
<meta charset="utf-8">
<title>Tarvel Build Letterhead</title>
<link href="https://fonts.googleapis.com/css2?family=Arimo:wght@400;700&display=swap" rel="stylesheet">
<style>
  :root {
    --amber: #fdb913;
    --slate: #6d6e71;
    --paper: #ffffff;
    --ink: #58595b;
  }
  html, body { margin: 0; padding: 0; overflow: hidden; }
  body { width: 927px; height: 1200px; background: var(--paper); font-family: "Arimo", Arial, sans-serif; }
  .letterhead { position: relative; width: 927px; height: 1200px; overflow: hidden; background: var(--paper); }
  .band { position: absolute; }
  .band--amber-left { left: 0; top: 73px; width: 69px; height: 64px; background: var(--amber); }
  .band--slate-left { left: 0; top: 143px; width: 69px; height: 65px; background: var(--slate); }
  .band--amber-main { left: 233px; top: 73px; width: 694px; height: 64px; background: var(--amber); }
  .band--slate-main { left: 233px; top: 143px; width: 694px; height: 65px; background: var(--slate); }
  .contact-panel { position: absolute; left: 694px; top: 60px; width: 200px; height: 83px; background: var(--paper); }
  .brand { position: absolute; left: 69px; top: 73px; width: 164px; height: 135px; background: var(--paper);
    display: flex; flex-direction: column; align-items: center; justify-content: center; gap: 12px; }
  .brand__mark { width: 56px; height: 56px; background: var(--amber); }
  .brand__name { color: var(--amber); font-weight: 700; font-size: 20px; letter-spacing: 1px; }
  .contact { position: absolute; right: 33px; top: 66px; margin: 0; padding: 0; list-style: none;
    text-align: right; color: var(--ink); font-size: 14.5px; line-height: 18px; }
  .contact li { display: flex; justify-content: flex-end; align-items: center; gap: 4px; white-space: nowrap; }
  .contact svg { width: 11px; height: 11px; flex: none; }
  .contact .gap { display: inline-block; width: 6px; }
  .contact .abn { padding-right: 17px; }
  .footer-slate { position: absolute; left: 0; top: 1174px; width: 927px; height: 26px; background: var(--slate); }
  .footer-amber { position: absolute; left: 241px; top: 1184px; width: 462px; height: 16px; background: var(--amber); }
</style>
</head>
<body>
<div class="letterhead">
  <div class="band band--amber-left"></div>
  <div class="band band--slate-left"></div>
  <div class="band band--amber-main"></div>
  <div class="band band--slate-main"></div>
  <div class="contact-panel"></div>

  <div class="brand">
    <div class="brand__mark"></div>
    <div class="brand__name">TARVEL BUILD</div>
  </div>

  <ul class="contact">
    <li>www.tarvelbuild.com.au
      <svg viewBox="0 0 12 12"><circle cx="6" cy="6" r="5" fill="none" stroke="#fdb913" stroke-width="1.4"/><line x1="1" y1="6" x2="11" y2="6" stroke="#fdb913"/><ellipse cx="6" cy="6" rx="2.2" ry="5" fill="none" stroke="#fdb913"/></svg>
    </li>
    <li>info@tarvelbuild.com.au
      <svg viewBox="0 0 12 12"><rect x="1" y="2.5" width="10" height="7" fill="none" stroke="#fdb913" stroke-width="1.2"/><polyline points="1,2.5 6,7 11,2.5" fill="none" stroke="#fdb913" stroke-width="1.2"/></svg>
    </li>
    <li>03 52631848
      <svg viewBox="0 0 12 12"><path d="M3 1 L5 3.5 L4 5 Q5.5 7.5 7 8 L8.5 7 L11 9 L9.5 11 Q4 10 1 3 Z" fill="#fdb913"/></svg>
      <span class="gap"></span>0413596281
      <svg viewBox="0 0 12 12"><rect x="3" y="1" width="6" height="10" rx="1" fill="none" stroke="#fdb913" stroke-width="1.4"/><circle cx="6" cy="9" r="0.8" fill="#fdb913"/></svg>
    </li>
    <li class="abn">47 318 965 102 - ABN</li>
  </ul>

  <div class="footer-slate"></div>
  <div class="footer-amber"></div>
</div>
</body>
</html>
```